Stationery Design Project - Tax Professionals/Ledger Guild

The name of our firm is “Penwick Group” and our slogan is “Bright Pathways”. You can also use the name "The Penwick Group" if it works better.

We are looking for a full stationery design: Letterhead, Business Card and With Compliments slip

We are looking for a bold, modern and clean/simple design that makes us stand out. We stand out as professionals in the industry and would like the stationery that our clients see to convey this image as well.

There is no colour preference.

We have used a "Lion" as our logo/symbol and that has received positive feedback from our clients; if you think the lion works then please incorporate the "lion".

If you think another symbol works then please submit this we are very open to ideas and would like to see designs that don't incorporate a lion as well.

We would like a corporate feel to this.

You could also incorporate the LG logo http://www.ledgerguildexample.com.au/Members/Marketing-your-practice/Logos but this is not a must.

WHO WE ARE:-
We are a Chartered Accounting firm who specialise in the delivery of taxation and strategic insolvency services. We also provide financial reporting services that help clients negotiate and compromise their debt or expenses such as rent with their landlords.

We work with Law Firms, other Accountants to deliver the best service for our clients.

Our clients come from varied backgrounds and are largely successful and established businesses and high net worth individuals looks for effective tax planning.

We are not the usual accounting firm and do not provide traditional tax return based services.
Updates

Reason: There are still designers who have signed on but not yet submitted designs and also adjustments to existing designs submitted. Extra time so designers are not rushed.

Target Market(s)

Corporate/ Independent successful businesses and individuals

Industry/Entity Type

Business

Requirements
Must have
• The letter must have the following phrase
“Liability limited by a scheme approved under Professional Standards Legislation”

The letter must also have the following business information:-
“The Penwick Group Pty Ltd atf
Principal - Colin T. Penwick
ABN: 47 215 708 362”

Plus Usual Address & Contact Details

We would also a logo or symbol that is representative of us. We like the idea of a lion but this is not set in stone and are very open to ideas.

```html
<!DOCTYPE html>
<html lang="en">
<head>
<meta charset="utf-8">
<title>The Penwick Group – Business Cards</title>
<link rel="stylesheet" href="https://fonts.googleapis.com/css2?family=Open+Sans:wght@400;600;700;800&display=swap">
<style>
  :root {
    --backdrop: #b08a2e;
    --card: #ffffff;
    --red: #e3061a;
    --red-deep: #c0153a;
    --red-bright: #ff0a0a;
    --charcoal: #3c3c3c;
    --ink: #222222;
    --grey-text: #555555;
    --logo-grey: #5a5a5a;
  }
  * { box-sizing: border-box; margin: 0; padding: 0; }
  html, body { width: 1200px; height: 686px; overflow: hidden; }
  body {
    background: var(--backdrop);
    font-family: "Open Sans", Arial, sans-serif;
    position: relative;
  }
  .card {
    position: absolute;
    width: 491px;
    height: 281px;
    background: var(--card);
    border-radius: 17px;
    overflow: hidden;
    box-shadow: 2px 3px 6px rgba(0,0,0,0.35);
  }
  .card--front { left: 81px; top: 107px; }
  .card--back  { left: 620px; top: 309px; width: 492px; height: 282px; }

  .lion-mark {
    position: absolute;
    background: radial-gradient(ellipse at 60% 45%, var(--red) 0%, #d8101e 55%, rgba(227,6,26,0.15) 100%);
    border-radius: 40% 45% 8% 8% / 55% 60% 10% 10%;
  }
  .ground-arc {
    position: absolute;
    height: 10px;
    border-top: 3px solid var(--red);
    border-radius: 50% 50% 0 0 / 100% 100% 0 0;
  }
  .wordmark {
    position: absolute;
    font-weight: 800;
    color: var(--logo-grey);
    letter-spacing: 0.5px;
    white-space: nowrap;
  }
  .slogan {
    position: absolute;
    font-weight: 400;
    color: var(--grey-text);
    letter-spacing: 3px;
    white-space: nowrap;
  }

  /* front card logo */
  .card--front .lion-mark { left: 52px; top: 50px; width: 175px; height: 78px; }
  .card--front .ground-arc { left: 38px; top: 129px; width: 212px; }
  .card--front .wordmark { left: 36px; top: 142px; font-size: 19px; }
  .card--front .slogan { left: 58px; top: 167px; font-size: 12px; }

  .divider {
    position: absolute;
    left: 280px; top: 64px;
    width: 1.5px; height: 133px;
    background: linear-gradient(to bottom, rgba(60,60,60,0), var(--charcoal) 25%, var(--charcoal) 75%, rgba(60,60,60,0));
  }
  .contact { position: absolute; left: 309px; top: 27px; color: var(--grey-text); }
  .contact__name { font-size: 15.5px; font-weight: 700; color: var(--red); line-height: 20px; }
  .contact__title { font-size: 12px; font-weight: 700; color: var(--ink); line-height: 16px; margin-bottom: 6px; }
  .contact__line { font-size: 12.5px; line-height: 16px; }
  .contact__list { list-style: none; margin-top: 8px; }
  .contact__list li { font-size: 12.5px; line-height: 19px; display: flex; align-items: center; gap: 5px; }
  .contact__list svg { width: 12px; height: 12px; flex: none; }

  .partner {
    position: absolute; left: 306px; top: 178px;
    display: flex; align-items: center; gap: 7px;
  }
  .partner__badge {
    width: 38px; height: 38px; border-radius: 50%;
    background: var(--red-deep);
    border: 3px solid #fff;
    box-shadow: 0 0 0 1.5px var(--red-deep);
  }
  .partner__name { font-size: 13px; font-weight: 700; color: var(--ink); }

  .wave { position: absolute; left: 0; bottom: 0; width: 100%; height: 100%; }
  .web {
    position: absolute;
    color: #fff; font-weight: 700; font-size: 11.5px; letter-spacing: 1.2px;
  }
  .card--front .web { left: 36px; top: 253px; }

  /* back card logo */
  .card--back .lion-mark { left: 138px; top: 46px; width: 228px; height: 92px; }
  .card--back .ground-arc { left: 123px; top: 140px; width: 250px; }
  .card--back .wordmark { left: 0; width: 100%; text-align: center; top: 148px; font-size: 21px; padding-left: 6px; }
  .card--back .slogan { left: 0; width: 100%; text-align: center; top: 175px; font-size: 13px; padding-left: 8px; }
  .card--back .web { left: 39px; top: 251px; }
</style>
</head>
<body>

  <section class="card card--front" aria-label="Business card, front">
    <div class="lion-mark" role="img" aria-label="Red striding lion illustration"></div>
    <div class="ground-arc"></div>
    <p class="wordmark">THE PENWICK GROUP</p>
    <p class="slogan">Bright Pathways</p>

    <div class="divider"></div>

    <div class="contact">
      <p class="contact__name">Your Name</p>
      <p class="contact__title">Title</p>
      <p class="contact__line">Street name</p>
      <p class="contact__line">City, State, zip code</p>
      <ul class="contact__list">
        <li>
          <svg viewBox="0 0 12 12" aria-hidden="true"><path d="M2.5 1 L4.5 1 L5.2 3.5 L4 4.5 C4.6 6 6 7.4 7.5 8 L8.5 6.8 L11 7.5 L11 9.5 C11 10.3 10.3 11 9.5 11 C5 11 1 7 1 2.5 C1 1.7 1.7 1 2.5 1 Z" fill="#e3061a"/></svg>
          123-456-7890
        </li>
        <li>
          <svg viewBox="0 0 12 12" aria-hidden="true"><rect x="3" y="1" width="6" height="4" fill="none" stroke="#e3061a" stroke-width="1.2"/><rect x="1" y="5" width="10" height="6" rx="1" fill="#e3061a"/><rect x="3" y="7" width="6" height="1" fill="#fff"/></svg>
          123-456-7890
        </li>
        <li>
          <svg viewBox="0 0 12 12" aria-hidden="true"><rect x="1" y="2.5" width="10" height="7" fill="#e3061a"/><path d="M1 2.5 L6 6.5 L11 2.5" fill="none" stroke="#fff" stroke-width="1"/></svg>
          name@website.com
        </li>
      </ul>
    </div>

    <div class="partner">
      <span class="partner__badge"></span>
      <span class="partner__name">Ledger Guild</span>
    </div>

    <svg class="wave" viewBox="0 0 491 281" preserveAspectRatio="none" aria-hidden="true">
      <defs>
        <linearGradient id="bandFront" x1="0" x2="1" y1="0" y2="0">
          <stop offset="0" stop-color="#c0153a"/>
          <stop offset="0.55" stop-color="#ff0a0a"/>
          <stop offset="1" stop-color="#d4102a"/>
        </linearGradient>
      </defs>
      <path d="M0 240 C110 222 230 232 320 256 C400 276 455 262 491 243 L491 281 L0 281 Z" fill="url(#bandFront)"/>
      <path d="M0 236 C110 216 230 226 320 250 C400 270 455 256 491 236" fill="none" stroke="#fff" stroke-width="3"/>
      <path d="M0 234 C110 212 230 222 320 246 C400 265 455 252 491 233" fill="none" stroke="#3c3c3c" stroke-width="4"/>
    </svg>
    <p class="web">www.website.com</p>
  </section>

  <section class="card card--back" aria-label="Business card, back">
    <div class="lion-mark" role="img" aria-label="Red striding lion illustration"></div>
    <div class="ground-arc"></div>
    <p class="wordmark">THE PENWICK GROUP</p>
    <p class="slogan">Bright Pathways</p>

    <svg class="wave" viewBox="0 0 492 282" preserveAspectRatio="none" aria-hidden="true">
      <defs>
        <linearGradient id="bandBack" x1="0" x2="1" y1="0" y2="0">
          <stop offset="0" stop-color="#c0153a"/>
          <stop offset="0.55" stop-color="#ff0a0a"/>
          <stop offset="1" stop-color="#d4102a"/>
        </linearGradient>
      </defs>
      <path d="M0 239 C110 221 230 231 320 255 C400 275 455 261 492 242 L492 282 L0 282 Z" fill="url(#bandBack)"/>
      <path d="M0 235 C110 215 230 225 320 249 C400 269 455 255 492 235" fill="none" stroke="#fff" stroke-width="3"/>
      <path d="M0 233 C110 211 230 221 320 245 C400 264 455 251 492 232" fill="none" stroke="#3c3c3c" stroke-width="4"/>
    </svg>
    <p class="web">www.website.com</p>
  </section>

</body>
</html>
```